Logo & Business card - Want to paint the town?

Brushvane - Top Quality Painting & Decorating

Brushvane are a painting & decorating company who work predominantly in the residential market and not commercial. We require a logo and business cards design

The company is based Christchurch NZ. Christchurch had major earthquakes in 2010 and 2011, which devastated the city. The city is in rebuild and fixing phase and will be for the next 5 years to get the city back on it's feet. As a result of the earthquakes are a lot of homes being fixed that require painting and decorating.

Additional to the earthquake work there is also huge growth in the city meaning lots of new homes are being built to accommodate the growth.

Alongside this there is an every growing rental market, so we not only work on residential earthquake repairs and new builds but also work with real estate agents, property managers and interior designers.

Christchurch has seen a large number of tradesmen enter the market and not all of whom are qualified/skilled. Our company’s painters are those with years of experience and who pride themselves on top quality precision work.

Brushvane are about quality jobs, done to a very high level at an affordable price. We are not the cheapest but also not the most expensive. Our logo and cards must reflect the quality of our work. Brushvane requires a professional logo and business card targeted to the higher end of the residential market.

Target Market(s)

Builders requiring contract painters, housing companies such as Tom Halvey, Kestrel buildings, Harbor Nest etc., real estate agents, property managers, interior designers and home owners.

The business cards and logo must appeal to builders, homeowner, interior designers and real estate agents so can’t be too masculine/feminine.

It needs to be bold, professional and stylish.

Industry/Entity Type

Residential

Logo Text

Brushvane

Logo styles of interest
Wordmark Logo
Requirements
Must have
• The logo and business cards must be bold, clean, modern, smart, simple, self explanatory, tidy, easy to read, timeless, and not frilly.

We are about quality, precision and being able to cut a straight line, so the card needs to avoid and curvy brush strokes as this denotes a bad a and sloppy painter.

The card and logo must scream top quality and affordability.
The card must be clean and modern, high end and stylish.

The logo must be something, which will go well on a silver/ black background as eventually as the van fleet will be either silver or black, so it must punch out on these colours.

For contact details that need to appear on the business cards see the full brief attached.
Nice to have
• One idea could be to have a picture on the business card of a well-painted stylish modern home interior, which would eventually be replaced by picture of Brushvane's paint jobs.
Should not have
• It definitely must not include is paint drips; paint pot with dribbles over the side of it, splurges of paint, or paintbrush swooshes as this indicates a messy painter.

Most colours are ok except for pink, orange or pastel colours.

```html
<!DOCTYPE html>
<html lang="en">
<head>
<meta charset="utf-8">
<title>Brushvane — Business Card</title>
<link rel="stylesheet" href="https://fonts.googleapis.com/css2?family=Open+Sans:wght@300;400;700&display=swap">
<style>
  :root {
    --stage: #2b2731;
    --card: #050505;
    --accent: #6a3fc8;
    --blue: #1fa7e0;
    --lime: #b8d433;
    --white: #ffffff;
    --grey: #9a9a9a;
    --divider: #5a5a5a;
    --font: "Open Sans", Arial, sans-serif;
  }
  * { box-sizing: border-box; margin: 0; padding: 0; }
  html, body { width: 1200px; height: 800px; overflow: hidden; }
  body {
    background: var(--stage);
    font-family: var(--font);
    display: flex;
    align-items: center;
    justify-content: center;
    gap: 40px;
  }
  .card {
    position: relative;
    width: 540px;
    height: 330px;
    background: var(--card);
    overflow: hidden;
    box-shadow: 0 10px 30px rgba(0,0,0,.35);
  }

  /* Wordmark */
  .wordmark {
    display: flex;
    align-items: center;
    gap: 10px;
    color: var(--lime);
    font-weight: 700;
    letter-spacing: -0.5px;
    white-space: nowrap;
  }
  .wordmark__dot {
    width: 12px; height: 12px;
    border-radius: 50%;
    background: var(--accent);
    flex: none;
  }

  /* Back */
  .card--back { display: flex; align-items: center; justify-content: center; }
  .card--back .wordmark { font-size: 64px; }
  .card--back .wordmark__dot { width: 18px; height: 18px; }

  /* Front */
  .top-band {
    position: absolute; left: 0; top: 0;
    width: 100%; height: 12px;
    background: var(--accent);
  }
  .person {
    position: absolute; left: 36px; top: 44px;
  }
  .person__name {
    font-size: 17px;
    color: var(--white);
    font-weight: 300;
    text-transform: uppercase;
    letter-spacing: .3px;
  }
  .person__first { color: var(--lime); font-weight: 700; }
  .person__role {
    font-size: 11px;
    color: var(--grey);
    margin-top: 2px;
  }
  .divider {
    position: absolute; left: 268px; top: 40px;
    width: 1px; height: 105px;
    background: var(--divider);
  }
  .brand-area {
    position: absolute; left: 269px; top: 40px;
    width: 271px; height: 105px;
    display: flex; align-items: center; justify-content: center;
  }
  .brand-area .wordmark { font-size: 38px; gap: 8px; }

  .contacts {
    position: absolute; left: 0; top: 178px;
    width: 100%;
    list-style: none;
  }
  .contact {
    display: flex;
    align-items: center;
    height: 24px;
    margin-bottom: 5px;
  }
  .contact__stub { width: 62px; height: 100%; }
  .contact__icon {
    width: 36px; height: 100%;
    display: flex; align-items: center; justify-content: center;
  }
  .contact__icon svg { width: 13px; height: 13px; }
  .contact__band {
    flex: 1; height: 100%;
    display: flex; align-items: center;
    padding-left: 10px;
    color: var(--white);
    font-size: 12px;
    font-weight: 400;
  }
  .contact--phone .contact__stub, .contact--phone .contact__band { background: var(--accent); }
  .contact--email .contact__stub, .contact--email .contact__band { background: var(--blue); }
  .contact--web .contact__stub, .contact--web .contact__band { background: var(--lime); }
  .contact--web .contact__band { color: var(--card); }
</style>
</head>
<body>

  <section class="card card--back" aria-label="Business card back">
    <div class="wordmark"><span>Brushvane</span><span class="wordmark__dot"></span></div>
  </section>

  <section class="card card--front" aria-label="Business card front">
    <div class="top-band"></div>

    <div class="person">
      <p class="person__name"><span class="person__first">Jenna</span> Corrick</p>
      <p class="person__role">Designation</p>
    </div>

    <div class="divider"></div>

    <div class="brand-area">
      <div class="wordmark"><span>Brushvane</span><span class="wordmark__dot"></span></div>
    </div>

    <ul class="contacts">
      <li class="contact contact--phone">
        <span class="contact__stub"></span>
        <span class="contact__icon">
          <svg viewBox="0 0 24 24" fill="#fff" aria-hidden="true"><path d="M6.6 10.8a15.1 15.1 0 0 0 6.6 6.6l2.2-2.2c.3-.3.7-.4 1-.2 1.1.4 2.3.6 3.6.6.6 0 1 .4 1 1V20c0 .6-.4 1-1 1A17 17 0 0 1 3 4c0-.6.4-1 1-1h3.5c.6 0 1 .4 1 1 0 1.3.2 2.5.6 3.6.1.3 0 .7-.2 1z"/></svg>
        </span>
        <span class="contact__band">021 47 38 12</span>
      </li>
      <li class="contact contact--email">
        <span class="contact__stub"></span>
        <span class="contact__icon">
          <svg viewBox="0 0 24 24" fill="none" stroke="#fff" stroke-width="2" aria-hidden="true"><rect x="3" y="5" width="18" height="14"/><path d="M3 5l9 8 9-8"/></svg>
        </span>
        <span class="contact__band">info@brushvane.co.nz</span>
      </li>
      <li class="contact contact--web">
        <span class="contact__stub"></span>
        <span class="contact__icon">
          <svg viewBox="0 0 24 24" fill="none" stroke="#fff" stroke-width="2" aria-hidden="true"><circle cx="12" cy="12" r="9"/><path d="M3 12h18M12 3c3 3 3 15 0 18M12 3c-3 3-3 15 0 18"/></svg>
        </span>
        <span class="contact__band">www.brushvane.co.nz</span>
      </li>
    </ul>
  </section>

</body>
</html>
```